business card for LWR pty ltd

We require a business card that stands out . I have included our company flyer and would like the services listed to be put on the card so when we Give out the cards to customers they have an idea of services we provide. need the winning design to be in editable photo shop format, editable iMac pages format or editable windows publisher format, so that I can enter in names, email addresses, phone numbers etc myself. I have included a pdf documents of info / items needed on the card to use as reference please.
Updates

need more submissions

Need extra days to review

Sick

Target Market(s)

new customers

Contact Information for Business Card

details are on attached business card requirements file

Requirements
Must have
• I have attached a list of must haves

```html
<!DOCTYPE html>
<html lang="en">
<head>
<meta charset="utf-8">
<title>LWR pty ltd — Business Card</title>
<link rel="stylesheet" href="https://fonts.googleapis.com/css2?family=Arimo:wght@700&family=Roboto+Condensed:wght@400;700&display=swap">
<style>
  :root {
    --page: #e4e4e4;
    --card: #0c0c0e;
    --card-edge: #1a1b1e;
    --ink: #ececec;
    --ink-soft: #d6d6d6;
    --accent: #b8691f;
    --rule: #3a3a3c;
    --logo: #a4a6a9;
  }
  * { box-sizing: border-box; margin: 0; padding: 0; }
  html, body { width: 1200px; height: 1200px; overflow: hidden; }
  body {
    background: var(--page);
    font-family: "Roboto Condensed", "Arial Narrow", sans-serif;
    color: var(--ink);
    position: relative;
  }
  .card {
    position: absolute;
    left: 257px;
    width: 686px;
    height: 392px;
    border-radius: 22px;
    overflow: hidden;
    background: radial-gradient(ellipse at 50% 40%, #232427 0%, var(--card) 70%);
    box-shadow: 0 14px 28px rgba(0,0,0,.25);
  }
  .card--front { top: 165px; }
  .card--back { top: 653px; background: linear-gradient(160deg, #17181a 0%, var(--card) 55%, #050506 100%); }

  /* Front */
  .front-texture {
    position: absolute; inset: 0 0 110px 0;
    background: radial-gradient(ellipse at 50% 45%, #3a3b3e 0%, #1b1c1e 45%, #0a0a0b 100%);
  }
  .front-wordmark {
    position: absolute; top: 62px; left: 0; right: 0;
    text-align: center;
    font-family: "Roboto Condensed", sans-serif;
    font-weight: 700;
    font-size: 128px;
    line-height: 1;
    letter-spacing: 4px;
    color: var(--logo);
  }
  .front-photo {
    position: absolute; left: 0; right: 0; bottom: 0; height: 180px;
    background: linear-gradient(180deg, rgba(20,20,20,0) 0%, #2a2520 35%, #8a5a35 62%, #b77d4f 82%, #a46a3e 100%);
  }

  /* Back */
  .person { position: absolute; left: 46px; top: 60px; }
  .person__name {
    font-family: "Arimo", sans-serif; font-weight: 700;
    font-size: 25px; color: var(--accent); letter-spacing: .3px;
  }
  .person__role { font-size: 16px; color: var(--ink); margin-top: 2px; }
  .fleet-photo {
    position: absolute; left: 479px; top: 54px; width: 158px; height: 90px;
    background: linear-gradient(90deg, #6f7479 0%, #9a9ea3 45%, #4a4c4f 70%, #c9c2b0 100%);
    border-radius: 4px;
    opacity: .85;
  }
  .rule { position: absolute; left: 46px; width: 589px; height: 1px; }
  .rule--grey { top: 128px; background: var(--rule); }
  .rule--accent { top: 223px; background: var(--accent); opacity: .8; }

  .company { position: absolute; left: 48px; top: 148px; font-size: 16px; line-height: 20px; color: var(--ink-soft); }
  .company__name { color: var(--accent); font-weight: 700; }

  .contact { position: absolute; left: 378px; top: 148px; list-style: none; font-size: 16px; line-height: 20px; color: var(--ink); }
  .contact li { display: flex; align-items: center; gap: 8px; }
  .contact svg { width: 12px; height: 12px; fill: var(--accent); flex: none; }

  .services { position: absolute; top: 240px; list-style: none; font-size: 16px; line-height: 19.4px; color: var(--ink-soft); }
  .services--left { left: 46px; }
  .services--right { left: 372px; top: 242px; }
  .services li::before, .dot::before {
    content: ""; display: inline-block; width: 5px; height: 5px; border-radius: 50%;
    background: var(--accent); margin: 0 8px 3px 0; vertical-align: middle;
  }
  .dot { margin-left: 5px; }
</style>
</head>
<body>

<section class="card card--front" aria-label="Business card front">
  <div class="front-texture" role="img" aria-label="Dark perforated metal texture background"></div>
  <div class="front-photo" role="img" aria-label="Photo of a road train with three tipper trailers on red outback dirt"></div>
  <div class="front-wordmark">LWR</div>
</section>

<section class="card card--back" aria-label="Business card back">
  <div class="person">
    <div class="person__name">DANIEL HARKER</div>
    <div class="person__role">Director</div>
  </div>
  <div class="fleet-photo" role="img" aria-label="Photo of two prime mover trucks"></div>

  <div class="rule rule--grey"></div>

  <div class="company">
    <div class="company__name">LWR pty ltd</div>
    <div>Lot 12, Wattle Street</div>
    <div>Broken Ridge, Australia</div>
  </div>

  <ul class="contact">
    <li><svg viewBox="0 0 24 24"><path d="M6.6 10.8a15.1 15.1 0 0 0 6.6 6.6l2.2-2.2a1 1 0 0 1 1-.25 11.4 11.4 0 0 0 3.6.57 1 1 0 0 1 1 1V20a1 1 0 0 1-1 1A17 17 0 0 1 3 4a1 1 0 0 1 1-1h3.5a1 1 0 0 1 1 1c0 1.25.2 2.45.57 3.57a1 1 0 0 1-.25 1z"/></svg>000 555 000</li>
    <li><svg viewBox="0 0 24 24"><path d="M2 5h20v14H2z M2 5l10 8 10-8" stroke="#0c0c0e" stroke-width="1.5"/></svg>info@lwrservices.com.au</li>
    <li><svg viewBox="0 0 24 24"><circle cx="12" cy="12" r="10"/><path d="M2 12h20M12 2c3 3 3 17 0 20M12 2c-3 3-3 17 0 20" stroke="#0c0c0e" stroke-width="1.5" fill="none"/></svg>lwrservices.com.au</li>
  </ul>

  <div class="rule rule--accent"></div>

  <ul class="services services--left">
    <li>Over size loads / Hot Shot Loads</li>
    <li>Heavy Vehicle Recovery services</li>
    <li>Potable Water Deliveries</li>
    <li>Road Building / Maintenance</li>
    <li>Earthworks<span class="dot">Sand &amp; Metal Supply &amp; Cartage</span></li>
  </ul>
  <ul class="services services--right">
    <li>Road Train Tippers</li>
    <li>Road Train Tankers</li>
    <li>Road Train Flat Tops</li>
    <li>Drop Deck Trailers</li>
    <li>Mine site accredited equipment &amp; Operators</li>
  </ul>
</section>

</body>
</html>
```